Website images and banners needed to be created

We have a website we have not used in a few months that need updated sales banners and images resized for our web devs to upload and update. The site in question is w w w . m a r p e l y . c o m

3 page

```html
<!DOCTYPE html>
<html lang="en">
<head>
<meta charset="utf-8">
<title>Black Friday Sale Banners</title>
<link rel="stylesheet" href="https://fonts.googleapis.com/css2?family=Bebas+Neue&family=Montserrat:wght@400;500;800&display=swap">
<style>
  :root {
    --stage: #b9b7b8;
    --ink: #0b0b0b;
    --ink-soft: #262626;
    --white: #ffffff;
    --red: #f50a0a;
    --red-deep: #c40000;
    --crimson: #e01a3c;
    --gold: #ffc700;
    --lime: #e4ef00;
    --ribbon-dark: #1c0b0b;
    --label: #2b2b2b;
    --silver: #d8d8d8;
  }
  html, body {
    margin: 0;
    width: 1200px;
    height: 880px;
    overflow: hidden;
    background: var(--stage);
  }
  .sheet { display: block; width: 1200px; height: 880px; }
  .label { font-family: "Montserrat", sans-serif; font-weight: 400; font-size: 31px; fill: var(--label); }
  .display { font-family: "Bebas Neue", sans-serif; }
  .heavy { font-family: "Montserrat", sans-serif; font-weight: 800; }
  .light { font-family: "Montserrat", sans-serif; font-weight: 400; }
  .fill-white { fill: var(--white); }
  .fill-red { fill: var(--red); }
  .fill-gold { fill: var(--gold); }
  .fill-ink { fill: var(--ink); }
</style>
</head>
<body>
<svg class="sheet" viewBox="0 0 1328 974" xmlns="http://www.w3.org/2000/svg" role="img" aria-label="Two Black Friday sale banners">
  <defs>
    <clipPath id="banner-one-area"><rect x="115" y="160" width="1098" height="312"/></clipPath>
    <clipPath id="banner-two-area"><rect x="115" y="530" width="1098" height="312"/></clipPath>
    <radialGradient id="floor-shadow" cx="50%" cy="50%" r="50%">
      <stop offset="0" stop-color="#000" stop-opacity=".28"/>
      <stop offset="1" stop-color="#000" stop-opacity="0"/>
    </radialGradient>
    <linearGradient id="chevron-metal" x1="0" y1="0" x2="0" y2="1">
      <stop offset="0" stop-color="#9c9c9c"/>
      <stop offset=".5" stop-color="#ffffff"/>
      <stop offset="1" stop-color="#8f8f8f"/>
    </linearGradient>
    <linearGradient id="red-panel" x1="0" y1="0" x2="1" y2="0">
      <stop offset="0" stop-color="var(--red-deep)"/>
      <stop offset=".35" stop-color="var(--red)"/>
    </linearGradient>
  </defs>

  <!-- Banner 1 -->
  <text class="label" x="720" y="139" text-anchor="middle">BANNER -1</text>
  <ellipse cx="664" cy="484" rx="560" ry="14" fill="url(#floor-shadow)"/>
  <g class="banner banner-one" clip-path="url(#banner-one-area)">
    <rect x="115" y="160" width="1098" height="312" fill="var(--ink)"/>
    <polygon class="chevron-metal" points="762,160 787,160 712,310 787,472 762,472 680,310" fill="url(#chevron-metal)"/>
    <polygon class="panel-red" points="787,160 1213,160 1213,472 787,472 712,310" fill="url(#red-panel)"/>
    <circle class="price-disc" cx="968" cy="312" r="176" fill="var(--ink)" stroke="var(--white)" stroke-width="13"/>
    <text class="display fill-white" x="866" y="362" font-size="232" textLength="176" lengthAdjust="spacingAndGlyphs">70</text>
    <text class="display fill-white" x="1044" y="268" font-size="84" textLength="44" lengthAdjust="spacingAndGlyphs">%</text>
    <text class="heavy" x="1081" y="359" font-size="36" fill="var(--lime)" transform="rotate(-90 1081 359)" textLength="72" lengthAdjust="spacingAndGlyphs">OFF</text>
    <polygon class="ribbon" points="803,394 1146,394 1154,450 795,450" fill="var(--red)"/>
    <text class="heavy fill-white" x="973" y="440" font-size="46" text-anchor="middle" textLength="306" lengthAdjust="spacingAndGlyphs">EVERYTHING</text>

    <polygon class="tag" points="196,197 345,197 361,217 345,238 180,238" fill="var(--red)"/>
    <text class="heavy fill-white" x="271" y="228" font-size="27" text-anchor="middle" textLength="120" lengthAdjust="spacingAndGlyphs">THE BIG</text>
    <rect x="370" y="215" width="293" height="3" fill="var(--white)"/>
    <text class="display fill-white" x="183" y="332" font-size="116" textLength="217" lengthAdjust="spacingAndGlyphs">BLACK</text>
    <text class="display fill-red" x="424" y="332" font-size="116" textLength="239" lengthAdjust="spacingAndGlyphs">FRIDAY</text>
    <rect x="186" y="358" width="276" height="3" fill="var(--white)"/>
    <polygon class="tag" points="475,365 498,342 655,342 638,365 655,388 498,388" fill="var(--red)"/>
    <text class="heavy fill-white" x="563" y="376" font-size="28" text-anchor="middle" textLength="98" lengthAdjust="spacingAndGlyphs">EVENT</text>
    <text class="light fill-white" x="182" y="443" font-size="40" textLength="230" lengthAdjust="spacingAndGlyphs">SALE MUST</text>
    <text class="heavy fill-red" x="426" y="443" font-size="40" textLength="226" lengthAdjust="spacingAndGlyphs">END SOON</text>
  </g>

  <!-- Banner 2 -->
  <ellipse cx="664" cy="854" rx="560" ry="14" fill="url(#floor-shadow)"/>
  <g class="banner banner-two" clip-path="url(#banner-two-area)">
    <rect x="115" y="530" width="1098" height="312" fill="var(--ink)"/>
    <polygon class="band-soft" points="115,530 1213,530 1213,532 115,650" fill="var(--ink-soft)"/>
    <circle class="price-disc" cx="280" cy="693" r="121" fill="var(--gold)"/>
    <g transform="rotate(-4 260 690)">
      <text class="display" x="188" y="748" font-size="172" fill="var(--crimson)" textLength="138" lengthAdjust="spacingAndGlyphs">70</text>
      <text class="display fill-ink" x="326" y="670" font-size="62" textLength="38" lengthAdjust="spacingAndGlyphs">%</text>
      <text class="heavy fill-ink" x="365" y="742" font-size="30" transform="rotate(-90 365 742)" textLength="60" lengthAdjust="spacingAndGlyphs">OFF</text>
    </g>
    <g transform="rotate(-10 293 776)">
      <polygon class="ribbon" points="160,750 430,750 422,802 152,802" fill="var(--ribbon-dark)"/>
      <text class="heavy fill-white" x="291" y="788" font-size="34" text-anchor="middle" textLength="222" lengthAdjust="spacingAndGlyphs">EVERYTHING</text>
    </g>
    <g transform="rotate(-7 352 828)">
      <text class="light fill-white" x="352" y="828" font-size="33" textLength="182" lengthAdjust="spacingAndGlyphs">SALE MUST</text>
      <text class="heavy fill-gold" x="544" y="828" font-size="33" textLength="176" lengthAdjust="spacingAndGlyphs">END SOON</text>
      <rect x="544" y="838" width="174" height="3" fill="var(--white)"/>
    </g>
    <g transform="rotate(-10 630 596)">
      <polygon class="tag" points="560,574 708,574 724,596 708,618 544,618 558,596" fill="var(--gold)"/>
      <text class="heavy fill-ink" x="632" y="607" font-size="27" text-anchor="middle" textLength="120" lengthAdjust="spacingAndGlyphs">THE BIG</text>
    </g>
    <text class="display fill-white" x="688" y="762" font-size="218" transform="rotate(-9 688 762)" textLength="440" lengthAdjust="spacingAndGlyphs">BLACK</text>
    <text class="display fill-white" x="798" y="834" font-size="132" transform="rotate(-11 798 834)" textLength="214" lengthAdjust="spacingAndGlyphs">FRIDAY</text>
    <g transform="rotate(-12 1100 752)">
      <polygon class="tag" points="1012,752 1034,728 1190,728 1174,752 1190,776 1034,776" fill="var(--gold)"/>
      <text class="heavy fill-ink" x="1104" y="763" font-size="29" text-anchor="middle" textLength="100" lengthAdjust="spacingAndGlyphs">EVENT</text>
    </g>
  </g>
  <text class="label" x="714" y="898" text-anchor="middle">BANNER -2</text>
</svg>
</body>
</html>
```